International Vacuum Business Needs a Business Card

We need a business card design for a new company based in Toronto called "Duvo-Sweep". We will be selling and installing a proprietary central vacuum system that is one of a kind to the condominium market mainly through various large builders throughout the country as well as a second distribution chain at a retail level. Our product has a very unique retractable hose system that allows the hose to be stored away within the walls of a space all by the push of a button. "No more hoses laying around the house" We would like to see the design use the colours Red, Black, Grey and possibly white. The design should communicate the following terms " sleek, discreet, convenient, sophisticated, modern"
Updates

Project Deadline Extended
Reason: Hello All, I have not been able to provide very much feedback as I have been unavailable this week so we will be extending the deadline for another 3 days. Thanks,

Project Deadline Extended
Reason: Hello All, The revision and feedback process has been slow so I have no choice but to extend once again. We are still looking for that one great design. Thank you

Project Deadline Extended
Reason: Guys the feedback and changes on some of the designs are taking really long from some of you so I have no choice but to continue extending the deadline forward.

Target Market(s)

Our target market is male/female aged 25-65, more so focussing on 25-50.

Industry/Entity Type

Retail

Requirements
Must have
• Phone #
Fax #
Mobile #
Toll Free #
Web site address "www.duvosweep.ca"

```html
<!DOCTYPE html>
<html lang="en">
<head>
<meta charset="utf-8">
<title>Duvo-Sweep Business Card</title>
<link href="https://fonts.googleapis.com/css2?family=Oswald:wght@300;400;500;600&display=swap" rel="stylesheet">
<style>
  :root {
    --page: #d9d6cf;
    --card-white: #f2f2f0;
    --ink: #2a2a2a;
    --black: #111111;
    --red: #a30d12;
    --grey: #8c8c8c;
    --grid: #d4d4d4;
  }
  html, body {
    margin: 0;
    width: 1200px;
    height: 948px;
    overflow: hidden;
    background: var(--page);
    font-family: "Oswald", sans-serif;
  }
  .stage {
    position: relative;
    width: 1200px;
    height: 948px;
  }
  .card {
    position: absolute;
    left: 290px;
    width: 620px;
    height: 354px;
    overflow: hidden;
    box-shadow: 0 6px 18px rgba(0,0,0,0.18);
  }
  /* ---------- back ---------- */
  .card-back {
    top: 80px;
    background: var(--black);
    color: #fff;
  }
  .card-back .pattern-area {
    position: absolute;
    right: 0;
    bottom: 0;
    width: 300px;
    height: 200px;
    background: radial-gradient(ellipse at 70% 60%, #2c2c2c 0%, #1a1a1a 50%, rgba(17,17,17,0) 80%);
  }
  .brand {
    position: absolute;
    display: flex;
    align-items: center;
    gap: 10px;
  }
  .brand-mark {
    width: 30px;
    height: 30px;
  }
  .brand-name {
    font-weight: 400;
    letter-spacing: 1px;
    line-height: 1;
  }
  .card-back .brand {
    left: 150px;
    top: 120px;
  }
  .card-back .brand-mark { background: #ffffff; width: 38px; height: 38px; }
  .card-back .brand-name { font-size: 48px; color: #ffffff; }
  .card-back .website {
    position: absolute;
    left: 270px;
    top: 200px;
    font-size: 15px;
    font-weight: 500;
    letter-spacing: 3px;
  }
  /* ---------- front ---------- */
  .card-front {
    top: 514px;
    background: var(--card-white);
    color: var(--ink);
  }
  .card-front .grid-area {
    position: absolute;
    left: 120px;
    top: 40px;
    width: 320px;
    height: 240px;
    background: radial-gradient(ellipse at 50% 50%, rgba(200,200,200,0.55) 0%, rgba(242,242,240,0) 70%);
  }
  .card-front .brand { left: 34px; top: 28px; }
  .card-front .brand-mark { background: var(--red); }
  .card-front .brand-name { font-size: 38px; color: var(--ink); }
  .name-band {
    position: absolute;
    left: 0;
    top: 96px;
    width: 310px;
    height: 46px;
    background: var(--black);
    clip-path: polygon(0 0, 100% 0, 92% 100%, 0 100%);
  }
  .person-name {
    position: absolute;
    left: 34px;
    top: 101px;
    font-size: 26px;
    font-weight: 500;
    color: var(--red);
    letter-spacing: 1px;
  }
  .title-band {
    position: absolute;
    left: 300px;
    top: 132px;
    width: 320px;
    height: 26px;
    background: var(--red);
    clip-path: polygon(4% 0, 100% 0, 100% 100%, 0 100%);
  }
  .job-title {
    position: absolute;
    left: 326px;
    top: 134px;
    font-size: 14px;
    font-weight: 400;
    color: var(--black);
  }
  .address {
    position: absolute;
    left: 34px;
    top: 160px;
    font-size: 13px;
    line-height: 1.35;
    text-transform: uppercase;
  }
  .address .company {
    font-size: 18px;
    font-weight: 600;
    text-decoration: underline;
    text-underline-offset: 3px;
    margin-bottom: 4px;
  }
  .contact-list {
    position: absolute;
    left: 376px;
    top: 178px;
    margin: 0;
    padding: 0;
    list-style: none;
    font-size: 16px;
    font-weight: 500;
    line-height: 24px;
  }
  .contact-list li {
    display: flex;
    align-items: center;
    gap: 12px;
  }
  .contact-list svg {
    width: 14px;
    height: 14px;
    fill: var(--ink);
    stroke: var(--ink);
  }
  .contact-list .note { font-weight: 400; font-size: 14px; }
  .footer-band {
    position: absolute;
    left: 0;
    bottom: 18px;
    width: 100%;
    height: 22px;
    background: var(--red);
  }
</style>
</head>
<body>
<main class="stage">

  <section class="card card-back" aria-label="Card back">
    <div class="pattern-area" role="img" aria-label="Fading checkered pattern in dark grey"></div>
    <div class="brand">
      <span class="brand-mark"></span>
      <span class="brand-name">Duvo-Sweep</span>
    </div>
    <div class="website">www.duvosweep.ca</div>
  </section>

  <section class="card card-front" aria-label="Card front">
    <div class="grid-area" role="img" aria-label="Light grey perspective grid of lines"></div>
    <div class="brand">
      <span class="brand-mark"></span>
      <span class="brand-name">Duvo-Sweep</span>
    </div>

    <div class="name-band"></div>
    <div class="person-name">MARCUS HALE</div>

    <div class="title-band"></div>
    <div class="job-title">Managing Director</div>

    <address class="address" style="font-style:normal">
      <div class="company">DUVO-SWEEP</div>
      48 Harbour Row, Suite 210<br>
      Toronto, ON M5J 0A1
    </address>

    <ul class="contact-list">
      <li>
        <svg viewBox="0 0 16 16" aria-hidden="true"><path stroke="none" d="M3 1h3l1 4-2 1.5a9 9 0 0 0 4.5 4.5L11 9l4 1v3c0 1-1 2-2 2C7 15 1 9 1 3c0-1 1-2 2-2z"/></svg>
        416.555.0142
      </li>
      <li>
        <svg viewBox="0 0 16 16" aria-hidden="true"><rect stroke="none" x="4" y="1" width="8" height="5"/><rect stroke="none" x="1" y="6" width="14" height="7" rx="1"/><rect x="4" y="10" width="8" height="5" fill="#fff" stroke-width="1"/></svg>
        416.555.0187
      </li>
      <li>
        <svg viewBox="0 0 16 16" aria-hidden="true"><rect x="4" y="1" width="8" height="14" rx="1.5" fill="none" stroke-width="1.6"/><circle stroke="none" cx="8" cy="12.5" r="1"/></svg>
        647.555.0119
      </li>
      <li>
        <svg viewBox="0 0 16 16" aria-hidden="true"><path d="M7 9l2-2M6 6L4 8a2.5 2.5 0 0 0 4 4l2-2M10 10l2-2a2.5 2.5 0 0 0-4-4L6 6" fill="none" stroke-width="1.6"/></svg>
        www.duvosweep.ca
      </li>
      <li>
        <svg viewBox="0 0 16 16" aria-hidden="true"><circle cx="8" cy="8" r="6.5" fill="none" stroke-width="1.4"/><path stroke="none" d="M6 4.5h1.5l.5 2-1 .8a4 4 0 0 0 1.8 1.8l.8-1 2 .5V10c0 .6-.5 1-1 1C7.5 11 5 8.5 5 5.5c0-.5.4-1 1-1z"/></svg>
        1.800.555.0163 <span class="note">(Toll Free)</span>
      </li>
    </ul>

    <div class="footer-band"></div>
  </section>

</main>
</body>
</html>
```